A unique communication angle to crowdfunding

Looking for a fresh redesign of a crowd funding website that deals in real estate. I already have the content, but am looking to take the design to the next level.

Existing real estate crowd funding sites focus on the real estate. I want to explore communication angle that:
- puts the investor in the centre of the communication: "become a baron"
- highlights the international nature (international properties, international investors)

There's also quite a lot of copy on the site, as we need to explain the service in quite a bit of detail. There's room to reduce the copy and replace with graphics. Could also consider clicking to see different text (see our difference section in http://galatownfeed.com)

The backend of the platform is already being worked on by a specialist crowd funding service provider.

In total there are 5 pages to be designed.

The homepage is really important. Right now it looks quite dated. It doesn't have a great layout. Note there is no mobile version of the website, so the pages need to be seen well on mobile devices. When looking at the brief, refer to the following links too:

current website:
http://pooltenant.com

some revisions made so far:
http://preview.fundmerrow.com/2G5GO2

Attached are logo files and another file which contained copy for the pages. No need to rework the logo.

Please make sure to use the same copy in the brief on the webpages, to ensure the layouts work. Designers are free to propose images they feel work on the pages.

I would like to see if rather than tweaking the pages, it's possible to come up with a better design concept. If the 5 pages are accepted, there's a chance I'll request an additional 4 pages.
Updates

Please note the font used in the logo is called "harabara" in case you decide to use it in any of the titles, etc.

Please note there is one additional page for which we would like to review designs. Note the page would be a template to be used on all future real estate detail pages. Here is an example of the current design for reference:

http://pooltenant.com/projects/view/14

In total there are 5 page designs required, (homepage + 4)

Thank you

FYI -

Just a quick note to give information from similar UK real estate crowdfunding sites:
http://www.estatewren.co.uk
http://plotharbor.co.uk
https://www.tilgarcap.com

Of the above, only plotharbor has a nice clean looking landing page. Information is clear and well laid out.

Hi all, just uploaded a new file in the brief. Contains some comments and a website reference. I thought it may help to explain how we could convey international aspect as well as how we could convey images in a more modern way. This is an option you can consider, but its entirely up to you how how answer the brief. Thanks!

We would like to let you know that we have just shortlisted the best designs. Together with that, we have also passed some detailed feedback to all designers who weren't shortlisted. If we didn't contact you, please let us know. If you haven't submitted a design or are working on revisions, please note these will no longer be taken into account now. We hope you understand that we need to close the project today. Thank you all once again for your great work and design concepts. Here's hoping we meet again on a future design brief. Cheers, pooltenant team.

Target Market(s)

At the moment, only rich are able to buy real estate. With this service, anyone can become a landlord. Target buyers:

Young professionals, looking to diversify from stock market and lower risk
People nearing retirement, looking for stable rental incomes
Retirees - looking to supplement pensions with possibility of capital gains
Parents - looking for a way to save long term for their children (instead of low interest paying bank accounts)

Industry/Entity Type

Communication

Font styles to use
Sans Serif
Other font styles liked:
• harabara

Colors
add136
f5f9eb
959595
000000

Requirements
Must have
• Overall, the site must convey "whoever you are, you too can become a landlord", and that you don't need to be wealthy to invest in real estate. See

Communication should put the investor (or the baron) at the centre. The investor can be any of those described in the target market.

Show the aspirational side of property ownership.

In addition to the investor/baron character, the second main theme is international. No other real estate crowdfunding website highlights this.
Nice to have
• Banner could show different consumer types, to illustrate that the service can appeal to many different profiles. Refer to attached file "home page reference - plainasdew.com" as an example of how this could be done.

Aim to show the international side of the service. Properties around the world, investors around the world.

```html
<!DOCTYPE html>
<html lang="en">
<head>
<meta charset="utf-8">
<title>pooltenant – become a property baron</title>
<link href="https://fonts.googleapis.com/css2?family=Open+Sans:wght@400;600;700&family=Varela+Round&display=swap" rel="stylesheet">
<style>
:root{
  --green:#8dc63f;
  --green-dark:#7ab32e;
  --green-pale:#f5f9eb;
  --ink:#222;
  --text:#555;
  --muted:#959595;
  --line:#e2e2e2;
  --band:#f4f4f4;
  --dark:#1f2124;
  --footer-bar:#444547;
  --white:#fff;
}
*{box-sizing:border-box;margin:0;padding:0}
html,body{width:1200px;height:3000px;overflow:hidden}
body{position:relative;background:var(--white);font-family:"Open Sans",Arial,sans-serif;color:var(--text);font-size:14px}
.heading{font-family:"Varela Round","Open Sans",sans-serif;color:var(--green);font-weight:400}
.abs{position:absolute}

/* header */
.site-header{position:absolute;left:0;top:0;width:1200px;height:100px}
.brand{left:130px;top:24px;display:flex;align-items:center;gap:10px}
.brand-mark{width:44px;height:44px;border-radius:50%;background:var(--green)}
.brand-name{font-family:"Varela Round",sans-serif;font-size:30px;color:var(--green)}
.follow{left:618px;top:26px;display:flex;align-items:center;gap:8px;font-size:13px;color:#666}
.social{width:30px;height:28px;background:var(--green)}
.social.alt{background:#eee}
.search{left:820px;top:24px;width:250px;height:30px;display:flex}
.search-field{flex:1;background:#efefef;font-size:11px;color:#aaa;padding:8px 10px}
.search-btn{width:38px;background:#555;display:flex;align-items:center;justify-content:center}
.main-nav{right:130px;top:72px;display:flex;gap:22px;font-size:11px;color:#555;text-transform:uppercase}
.main-nav a{color:inherit;text-decoration:none;padding-bottom:6px}
.main-nav a.active{color:#222;font-weight:700;border-bottom:2px solid var(--green)}

/* hero */
.hero{left:0;top:100px;width:1200px;height:400px;background:linear-gradient(180deg,#8fb0cf 0%,#c9d8e6 28%,#d7a89a 45%,#c48e82 62%,#7c9a58 82%,#6a8c46 100%)}
.hero-arrow{top:180px;width:44px;height:44px;border-radius:50%;background:rgba(0,0,0,.75);display:flex;align-items:center;justify-content:center}
.hero-caption{left:145px;top:290px;width:505px;height:72px;background:rgba(0,0,0,.7);padding:10px 14px}
.hero-caption h1{font-family:"Varela Round",sans-serif;font-weight:400;font-size:26px;color:var(--white);line-height:30px}
.hero-caption h1 span{color:var(--green)}
.hero-caption p{font-size:15px;color:var(--green);line-height:20px}
.hero-dots{left:116px;top:380px;display:flex;gap:6px}
.hero-dots i{width:9px;height:9px;border-radius:50%;background:#888}
.hero-dots i.on{background:var(--green)}

/* intro */
.intro{left:0;top:500px;width:1200px;text-align:center}
.intro h2{font-size:30px;margin-top:50px}
.intro hr{width:640px;margin:14px auto 18px;border:0;border-top:1px solid var(--line)}
.intro p{font-size:14px;line-height:24px;color:#666;margin:0 auto 24px;width:800px}
.intro b{color:var(--green);font-weight:600}

/* paths */
.paths{left:0;top:816px;width:1200px;height:308px;background:var(--band)}
.path-card{top:52px;width:380px;height:200px;background:var(--white);border:1px solid var(--line)}
.path-icon{position:absolute;left:18px;top:26px;width:78px;height:78px;border-radius:50%;background:#3a3a3a;display:flex;align-items:center;justify-content:center}
.path-card h3{position:absolute;left:118px;top:26px;font-size:22px}
.path-card p{position:absolute;left:118px;top:60px;width:240px;font-size:13px;line-height:24px;color:#666}
.path-btn{position:absolute;left:0;bottom:0;width:100%;height:54px;background:var(--green);color:#2b3a14;font-family:"Varela Round",sans-serif;font-size:21px;display:flex;align-items:center;justify-content:center}

/* projects */
.projects{left:0;top:1124px;width:1200px;height:650px;text-align:center}
.projects h2{font-size:21px;margin-top:30px}
.projects .lead{font-size:13px;line-height:26px;color:#666;margin-top:8px}
.projects .lead b{color:var(--green);font-weight:600}
.project{top:154px;width:302px;height:432px;background:var(--white);border:1px solid var(--line);text-align:left}
.project.raised{box-shadow:0 2px 8px rgba(0,0,0,.25)}
.project-photo{position:absolute;left:0;top:0;width:100%;height:210px}
.tag-price{position:absolute;left:0;top:0;background:var(--green);color:var(--white);font-size:12px;font-weight:700;padding:4px 8px}
.tag-new{position:absolute;left:0;top:34px;background:#555;color:#e7f3d4;font-size:10px;padding:3px 8px}
.project h4{position:absolute;left:18px;top:226px;font-size:15px;font-weight:600;color:var(--green)}
.project .summary{position:absolute;left:18px;top:256px;width:266px;font-size:12px;line-height:20px;color:#666}
.project .rule{position:absolute;left:0;top:328px;width:100%;border-top:1px solid var(--line)}
.funded{position:absolute;left:14px;top:342px;font-size:14px;font-weight:600;color:#333}
.bar{position:absolute;left:14px;top:364px;width:276px;height:20px;border:1px solid #ccc;border-radius:3px;background:var(--white);overflow:hidden}
.bar i{display:block;height:100%;background:var(--green);font-style:normal;font-size:12px;font-weight:600;color:#333;text-align:right;padding-right:8px;line-height:18px}
.bar span{position:absolute;top:0;font-size:12px;font-weight:600;color:#333;line-height:18px}
.details{position:absolute;left:0;top:398px;width:100%;text-align:center;font-size:13px;color:#666}
.details.strong{color:var(--green);font-weight:700}

/* community */
.community{left:0;top:1774px;width:1200px;height:436px;background:linear-gradient(180deg,#2a2c2f 0%,#1b1c1e 60%,#111 100%);text-align:center}
.community h2{font-size:22px;margin-top:56px}
.community .lead{width:640px;margin:14px auto 0;color:#aaa;font-size:15px;line-height:24px}
.feature{top:180px;width:260px}
.feature-art{width:150px;height:150px;margin:0 auto;border-radius:50%;background:radial-gradient(circle,#eaeaea 0%,#bdbdbd 60%,rgba(0,0,0,0) 72%)}
.feature p{margin-top:24px;color:#999;font-size:15px;line-height:24px}

/* press */
.press{left:130px;top:2270px;width:940px;height:200px;border:1px solid var(--line)}
.press-tab{position:absolute;left:390px;top:-18px;width:180px;height:38px;background:var(--green);color:#2a3a12;font-size:17px;font-weight:600;display:flex;align-items:center;justify-content:center}
.badge{position:absolute;height:30px;background:#d6d6d6;border-radius:3px}

/* footer */
.footer-bar{left:0;top:2516px;width:1200px;height:72px;background:var(--footer-bar)}
.footer-follow{left:130px;top:22px;display:flex;align-items:center;gap:10px;color:var(--green);font-size:17px;font-weight:600}
.footer-follow .social{width:36px;height:30px;background:none;border:2px solid var(--green)}
.copyright{right:130px;top:26px;color:var(--green);font-size:13px;font-weight:600}
.footer-info{left:0;top:2588px;width:1200px;height:412px;background:var(--band)}
.footer-info p{position:absolute;left:130px;font-size:13px;line-height:24px;color:#555}
.footer-info b{color:var(--green);font-weight:700}
.partner{left:852px;top:36px;font-size:34px;color:#555}
</style>
</head>
<body>

<header class="site-header">
  <div class="abs brand"><span class="brand-mark"></span><span class="brand-name">pooltenant</span></div>
  <div class="abs follow">Follow us on <span class="social"></span><span class="social alt"></span></div>
  <div class="abs search">
    <div class="search-field">Search...</div>
    <div class="search-btn"><svg width="16" height="16" viewBox="0 0 16 16"><circle cx="6.5" cy="6.5" r="4.5" fill="none" stroke="#fff" stroke-width="2"/><line x1="10" y1="10" x2="14" y2="14" stroke="#fff" stroke-width="2"/></svg></div>
  </div>
  <nav class="abs main-nav">
    <a class="active">Home</a><a>Sign in</a><a>How it works</a><a>Discover a project</a><a>The Baron</a><a>Blog</a><a>Find out more</a>
  </nav>
</header>

<section class="abs hero" role="img" aria-label="Photo of a smiling family of four standing in front of a pink suburban house with palm trees">
  <div class="abs hero-arrow" style="left:76px"><svg width="14" height="14" viewBox="0 0 14 14"><path d="M9 2 4 7l5 5" fill="none" stroke="#8dc63f" stroke-width="2.5"/></svg></div>
  <div class="abs hero-arrow" style="left:1078px"><svg width="14" height="14" viewBox="0 0 14 14"><path d="M5 2l5 5-5 5" fill="none" stroke="#8dc63f" stroke-width="2.5"/></svg></div>
  <div class="abs hero-caption">
    <h1>Welcom to <span>pooltenant</span></h1>
    <p>Lorem Ipsum is simply dummy text of the printing and typesetting industry.</p>
  </div>
  <div class="abs hero-dots"><i class="on"></i><i></i><i></i><i></i></div>
</section>

<section class="abs intro">
  <h2 class="heading">Reconstructing a property ladder that´s strong and fair</h2>
  <hr>
  <p>By harnessing the power of crowds, it's possible to become a landlord in locations around the world. Forget the burden of financing <b>100%</b> of the purchase.</p>
  <p>Leave the day to day management of your property portfolio to us.</p>
  <p>Start with <b>1%</b> in a project and plan your steps to becoming a true baron</p>
</section>

<section class="abs paths">
  <div class="abs path-card" style="left:190px">
    <div class="path-icon"><svg width="40" height="44" viewBox="0 0 40 44"><rect x="4" y="16" width="10" height="26" fill="#8dc63f"/><rect x="16" y="4" width="12" height="38" fill="#8dc63f"/><rect x="30" y="20" width="8" height="22" fill="#8dc63f"/></svg></div>
    <h3 class="heading">Find properties</h3>
    <p>Sign up to browse the portfolio. Your journey to becoming a real estate baron starts here.</p>
    <div class="path-btn">Become a member</div>
  </div>
  <div class="abs path-card" style="left:630px">
    <div class="path-icon"><svg width="42" height="40" viewBox="0 0 42 40"><path d="M4 20 21 5l17 15v17H4z" fill="#8dc63f"/><rect x="16" y="24" width="10" height="13" fill="#3a3a3a"/></svg></div>
    <h3 class="heading">Find Buyers</h3>
    <p>Submit a property or development and raise funds from our real estate barons.</p>
    <div class="path-btn">Submit a property</div>
  </div>
</section>

<section class="abs projects">
  <h2 class="heading">Featured Projects</h2>
  <p class="lead">Brief details of new and popular projects. To view full listings, you will be required to<br>sign up and <b>become a member.</b></p>

  <article class="abs project raised" style="left:128px">
    <div class="project-photo" role="img" aria-label="Photo of a red brick two-storey house with a double garage" style="background:linear-gradient(180deg,#5d8fd0 0%,#9bbbe0 35%,#9a5a3e 55%,#7d4a34 75%,#8a8a7a 100%)"></div>
    <span class="tag-price">From GBP 3,600</span><span class="tag-new">New Launch</span>
    <h4>21 Fennel Row LONDON E1</h4>
    <p class="summary">Lorem Ipsum is simply dummy text of the printing and typesetting industry. Lorem Ipsum has been the industry's ..</p>
    <div class="rule"></div>
    <div class="funded">Funded</div>
    <div class="bar"><i style="width:50%">50%</i></div>
    <div class="details strong">See Project Details</div>
  </article>

  <article class="abs project" style="left:449px">
    <div class="project-photo" role="img" aria-label="Photo of a beige and brick suburban house with a lawn" style="background:linear-gradient(180deg,#5f94d6 0%,#a9c4e2 35%,#b99c86 55%,#d8c8b0 72%,#6f9a45 100%)"></div>
    <span class="tag-price">From GBP 3,600</span><span class="tag-new">New Launch</span>
    <h4>21 Fennel Row LONDON E1</h4>
    <p class="summary">Lorem Ipsum is simply dummy text of the printing and typesetting industry. Lorem Ipsum has been the industry's ..</p>
    <div class="rule"></div>
    <div class="funded">Funded</div>
    <div class="bar"><i style="width:75%">75%</i></div>
    <div class="details">See Project Details</div>
  </article>

  <article class="abs project" style="left:770px">
    <div class="project-photo" role="img" aria-label="Photo of a white Mediterranean villa with terracotta roofs and trees" style="background:linear-gradient(180deg,#4f8ad6 0%,#9cc0e6 30%,#e9e2d2 55%,#b86a45 68%,#5d8038 100%)"></div>
    <span class="tag-price">From GBP 3,600</span><span class="tag-new">New Launch</span>
    <h4>21 Fennel Row LONDON E1</h4>
    <p class="summary">Lorem Ipsum is simply dummy text of the printing and typesetting industry. Lorem Ipsum has been the industry's ..</p>
    <div class="rule"></div>
    <div class="funded">Funded</div>
    <div class="bar"><i style="width:40%"></i><span style="left:122px">40%</span></div>
    <div class="details">See Project Details</div>
  </article>
</section>

<section class="abs community" role="group" aria-label="Community">
  <h2 class="heading">Be Part of a Growing International Community</h2>
  <p class="lead">Gain access to new projects in world class cities and join our growing community of international landlords.</p>
  <div class="abs feature" style="left:160px">
    <div class="feature-art" role="img" aria-label="Illustration of a world map with a location pin"></div>
    <p>A community of international<br>property barons.</p>
  </div>
  <div class="abs feature" style="left:470px">
    <div class="feature-art" role="img" aria-label="Illustration of a group of people joined by a green ring"></div>
    <p>Collective buying power of<br>the pooltenant community</p>
  </div>
  <div class="abs feature" style="left:790px">
    <div class="feature-art" role="img" aria-label="Illustration of a world map with a location pin"></div>
    <p>Attractive real estate from<br>around the world</p>
  </div>
</section>

<section class="abs press" aria-label="Featured In">
  <div class="press-tab">Featured In</div>
  <span class="badge" style="left:38px;top:66px;width:116px"></span>
  <span class="badge" style="left:184px;top:66px;width:118px"></span>
  <span class="badge" style="left:338px;top:66px;width:118px"></span>
  <span class="badge" style="left:556px;top:66px;width:350px"></span>
  <span class="badge" style="left:150px;top:136px;width:80px;height:36px"></span>
  <span class="badge" style="left:268px;top:140px;width:132px"></span>
  <span class="badge" style="left:428px;top:134px;width:42px;height:40px"></span>
  <span class="badge" style="left:498px;top:134px;width:56px;height:40px"></span>
  <span class="badge" style="left:608px;top:138px;width:122px"></span>
</section>

<footer>
  <div class="abs footer-bar">
    <div class="abs footer-follow">Follow us on <span class="social"></span><span class="social"></span></div>
    <div class="abs copyright">© pooltenant 2014</div>
  </div>
  <div class="abs footer-info">
    <p style="top:22px;width:620px"><b>Pool Tenant</b> is part of the Tallow Ridge Group. The Tallow Ridge Group is a worldwide pioneer and leader in the crowd investing, peer to peer and online investment market.</p>
    <div class="abs partner">Tallow Ridge</div>
    <p style="top:100px;width:940px">By accessing this site and any pages thereof, you agree to be bound by the terms and conditions. This website is only suitable, intended and available for professional or sophisticated, or similar investors in other jurisdictions, or those who are members of pooltenant community and familiar with, and willing to, accept the risks associated with private participation. Pooltenant does not endorse any of the projects that appear on this website, nor does it make any recommendations regarding the appropriateness of particular opportunities for any participant. Each potential participant must review and evaluate the projects in his or her own discretion and determine the suitability of participating.</p>
    <p style="top:250px;width:940px">This website (the "Site") is in every respect unaffiliated with any site to which it links or to any company or entity (and connected projects, investment opportunity or similar) featured on this Site, and is not meant as an endorsement of any of those companies or entities ("third parties"). Furthermore and for the avoidance of doubt, Pooltenant Limited is in no way affiliated with any third parties featured or referenced on this Site. There is no commercial relationship between Pooltenant Limited and such third parties, nor an agency arrangement or similar. If you believe your Content (including third party content) as each such term is defined in our Terms of Service has been reproduced on the Site without permission, please refer to our Terms of Service for information on how to request its removal from the Site.</p>
  </div>
</footer>

</body>
</html>
```